Logo and label lay out for Copper Thistle wines

Wine Bottle label for single vineyard on The Mornington Peninsula, Victoria, Australia
Name of Vineyard is “Copper Thistle”
(A copper Thistle is a common biting ant found in the vineyard.)
The name and vintage of each of the four varieties of wine will need to be included on the label.
We want an instantly recognisable image on the label along with the name Copper Thistle.

Target Market(s)

Quality wine for cafes, restaurants and individual’s wine collection

Industry/Entity Type

Vineyard

Logo Text

Copper Thistle

Logo styles of interest
Emblem Logo
Abstract Logo
Colors

Designer to choose colors to be used in the design.

Requirements
Must have
• Simple yet stylish image, instantly recognisable .
Nice to have
• Possibly a stylistic image of an ant
Should not have
• Not an overly detailed image.

```html
<!DOCTYPE html>
<html lang="en">
<head>
<meta charset="utf-8">
<title>Copper Thistle — Wine Label</title>
<link rel="stylesheet" href="https://fonts.googleapis.com/css2?family=Kaushan+Script&family=Montserrat:wght@600&display=swap">
<style>
  :root {
    --page: #ffffff;
    --label: #070707;
    --gold: #d6a04a;
    --gold-line: #b8843a;
  }
  html, body {
    margin: 0;
    padding: 0;
    width: 999px;
    height: 1200px;
    overflow: hidden;
    background: var(--page);
  }
  .canvas {
    position: relative;
    width: 999px;
    height: 1200px;
  }
  .label {
    position: absolute;
    left: 200px;
    top: 100px;
    width: 600px;
    height: 1000px;
    background: var(--label);
  }
  .label__frame {
    position: absolute;
    inset: 0;
  }
  .label__mark {
    position: absolute;
    left: 50%;
    top: 240px;
    width: 150px;
    height: 150px;
    margin-left: -75px;
    border-radius: 50%;
    background: var(--gold);
  }
  .label__name {
    position: absolute;
    left: 0;
    right: 0;
    top: 455px;
    margin: 0;
    text-align: center;
    font-family: "Kaushan Script", cursive;
    font-weight: 400;
    font-size: 100px;
    line-height: 135px;
    color: var(--gold);
  }
  .label__volume {
    position: absolute;
    left: 0;
    right: 0;
    top: 826px;
    margin: 0;
    text-align: center;
    font-family: "Montserrat", sans-serif;
    font-weight: 600;
    font-size: 24px;
    letter-spacing: 0.5px;
    color: var(--gold);
  }
</style>
</head>
<body>
  <main class="canvas">
    <section class="label">
      <svg class="label__frame" width="600" height="1000" viewBox="0 0 600 1000" aria-hidden="true">
        <path d="M70 50 H530 A28 28 0 0 0 558 78 V852 A28 28 0 0 0 530 880 H70 A28 28 0 0 0 42 852 V78 A28 28 0 0 0 70 50 Z"
              fill="none" stroke="var(--gold-line)" stroke-width="3"/>
      </svg>
      <div class="label__mark"></div>
      <h1 class="label__name">Copper<br>Thistle</h1>
      <p class="label__volume">750ML</p>
    </section>
  </main>
</body>
</html>
```